Vorlan cards

I am in the auto motive, transportation business I would like a business card that is Something cool, modern edgy, having to do with car culture. I offer towing service for high and exotic cars. I also provide towing for collisions and car accidents. I offer open and enclosed transport nationwide.

Target Market(s)

Car culture people high end auto collectors

Industry/Entity Type

Towing car carrier

Contact Information for Business Card

My company colors black yellow and silver

Font styles to use
Serif

```html
<!DOCTYPE html>
<html lang="en">
<head>
<meta charset="UTF-8">
<title>Vorlan Business Card</title>
<link href="https://fonts.googleapis.com/css2?family=Poppins:wght@400;600&display=swap" rel="stylesheet">
<style>
  :root {
    --bg: #e9e7e5;
    --black: #000000;
    --yellow: #f9dc55;
    --name-yellow: #f6d94a;
    --white: #ffffff;
    --silver-light: #f4f2f2;
    --silver-mid: #d9d5d6;
    --silver-dark: #a9a6a8;
  }
  * { margin: 0; padding: 0; box-sizing: border-box; }
  html, body {
    width: 1200px;
    height: 900px;
    overflow: hidden;
    background: var(--bg);
    font-family: "Poppins", sans-serif;
  }
  .card {
    position: absolute;
    left: 100px;
    top: 141px;
    width: 1000px;
    height: 617px;
    background: var(--black);
    overflow: hidden;
    box-shadow: 0 10px 30px rgba(0,0,0,0.18);
  }
  .card__accent {
    position: absolute;
    left: 678px;
    top: 0;
    width: 322px;
    height: 100%;
    background: var(--yellow);
  }
  .card__seal {
    position: absolute;
    left: 412px;
    top: 42px;
    width: 532px;
    height: 532px;
    border-radius: 50%;
    background: radial-gradient(circle at 40% 38%, var(--silver-light) 0%, var(--silver-mid) 60%, var(--silver-dark) 100%);
    display: flex;
    align-items: center;
    justify-content: center;
  }
  .brand-name {
    font-family: "Poppins", sans-serif;
    font-weight: 600;
    font-size: 78px;
    letter-spacing: 2px;
    color: var(--black);
  }
  .person {
    position: absolute;
    left: 59px;
    top: 64px;
  }
  .person__name {
    font-weight: 600;
    font-size: 40px;
    line-height: 1.1;
    color: var(--name-yellow);
    letter-spacing: 0.5px;
  }
  .person__title {
    font-weight: 400;
    font-size: 28px;
    line-height: 1.2;
    color: var(--white);
  }
  .address {
    position: absolute;
    left: 60px;
    top: 252px;
    font-size: 28px;
    font-style: normal;
    line-height: 37px;
    color: var(--white);
  }
  .contacts {
    position: absolute;
    left: 59px;
    top: 446px;
    list-style: none;
    font-size: 28px;
    line-height: 37px;
    color: var(--white);
  }
  .contacts__item {
    display: flex;
    align-items: center;
    gap: 9px;
  }
  .contacts__icon {
    width: 26px;
    height: 26px;
    flex: none;
  }
</style>
</head>
<body>
  <div class="card">
    <div class="card__accent"></div>
    <div class="card__seal">
      <span class="brand-name">VORLAN</span>
    </div>

    <div class="person">
      <div class="person__name">DORIAN KESSLER</div>
      <div class="person__title">Managing Director</div>
    </div>

    <address class="address">
      318, Harbor Lane<br>
      North<br>
      60417,Eastmoor Ridge
    </address>

    <ul class="contacts">
      <li class="contacts__item">
        <svg class="contacts__icon" viewBox="0 0 24 24" aria-hidden="true">
          <path fill="var(--yellow)" d="M6.6 10.8a15.1 15.1 0 0 0 6.6 6.6l2.2-2.2a1 1 0 0 1 1-.25 11.4 11.4 0 0 0 3.6.57 1 1 0 0 1 1 1V20a1 1 0 0 1-1 1A17 17 0 0 1 3 4a1 1 0 0 1 1-1h3.5a1 1 0 0 1 1 1c0 1.25.2 2.45.57 3.57a1 1 0 0 1-.25 1z"/>
          <path fill="none" stroke="var(--yellow)" stroke-width="1.8" d="M14 3.5a7 7 0 0 1 6.5 6.5M14 7a3.5 3.5 0 0 1 3 3"/>
        </svg>
        <span>052-318 640 217</span>
      </li>
      <li class="contacts__item">
        <svg class="contacts__icon" viewBox="0 0 24 24" aria-hidden="true">
          <rect x="2" y="5" width="20" height="14" fill="var(--yellow)"/>
          <path d="M2 5l10 8 10-8" fill="none" stroke="var(--black)" stroke-width="1.6"/>
        </svg>
        <span>desk@vorlan.com</span>
      </li>
      <li class="contacts__item">
        <svg class="contacts__icon" viewBox="0 0 24 24" aria-hidden="true">
          <g fill="none" stroke="var(--yellow)" stroke-width="1.8">
            <circle cx="12" cy="12" r="9.5"/>
            <ellipse cx="12" cy="12" rx="4.5" ry="9.5"/>
            <path d="M2.5 12h19M4 7h16M4 17h16"/>
          </g>
        </svg>
        <span>www.vorlantow.com</span>
      </li>
    </ul>
  </div>
</body>
</html>
```